tiling company needs letterhead urgent

We need a logo to represent our company on an electronic letterhead. We are a tiling firm called Corwell Tiling Ltd and undertake all aspects of tiling work. The final design of the logo should incorporate the type of work we do and should be modern. We do not want any designs which may be considered 'novelty' or 'cartoonish.' No characters please, we require something sleek and contemporary . Please ensure the company name is central to your design ,Corwell Tiling Ltd

Industry/Entity Type

Electronic

Requirements
Must have
• text on letterhead to included

Registered address 41 Birch lane Failsworth Manchester M359QT
Company number 5267093
VAT no 412957386
Mobile no 07831659047
Office no 0161 574 8192
Web :www.floorvane.co.uk
Email : gareth@floorvane.co.uk
Nice to have
• a tile theme

```html
<!DOCTYPE html>
<html lang="en">
<head>
<meta charset="utf-8">
<title>Corwell Tiling Ltd – Letterhead</title>
<link rel="stylesheet" href="https://fonts.googleapis.com/css2?family=Arimo:wght@400;700&display=swap">
<style>
  :root {
    --navy: #23237d;
    --rust: #b5533c;
    --paper: #ffffff;
    --s1: #23237d; --s2: #2f2f85; --s3: #3d3d8d; --s4: #4c4c96;
    --s5: #5d5da0; --s6: #7070ab; --s7: #8585b8; --s8: #9b9bc6;
    --s9: #b3b3d4; --s10: #cbcbe2; --s11: #e0e0ee; --s12: #eeeef6; --s13: #f5f5fa;
  }
  * { margin: 0; padding: 0; box-sizing: border-box; }
  html, body { width: 934px; height: 1200px; overflow: hidden; background: var(--paper); }
  body { font-family: "Arimo", Arial, sans-serif; color: var(--navy); }
  .letterhead { position: relative; width: 934px; height: 1200px; }

  .brand { position: absolute; left: 85px; top: 150px; display: flex; align-items: center; gap: 10px; }
  .brand-mark { width: 24px; height: 24px; background: var(--rust); }
  .brand-name { font-weight: 700; font-size: 15px; letter-spacing: 0.3px; color: var(--navy); }

  .rule { position: absolute; left: 78px; width: 789px; height: 8px; display: flex; }
  .rule span { flex: 1; }
  .rule span:nth-child(1) { background: var(--s1); }
  .rule span:nth-child(2) { background: var(--s2); }
  .rule span:nth-child(3) { background: var(--s3); }
  .rule span:nth-child(4) { background: var(--s4); }
  .rule span:nth-child(5) { background: var(--s5); }
  .rule span:nth-child(6) { background: var(--s6); }
  .rule span:nth-child(7) { background: var(--s7); }
  .rule span:nth-child(8) { background: var(--s8); }
  .rule span:nth-child(9) { background: var(--s9); }
  .rule span:nth-child(10) { background: var(--s10); }
  .rule span:nth-child(11) { background: var(--s11); }
  .rule span:nth-child(12) { background: var(--s12); }
  .rule span:nth-child(13) { background: var(--s13); }
  .rule-top { top: 213px; }
  .rule-bottom { top: 1080px; }

  .footer { position: absolute; top: 1104px; left: 78px; right: 60px; font-size: 16px; line-height: 22px; }
  .registered { position: absolute; left: 0; top: 0; width: 420px; }
  .registered .row { display: flex; }
  .registered .label { width: 102px; }
  .contact { position: absolute; left: 441px; top: 0; display: grid; grid-template-columns: 130px auto; row-gap: 1px; }
</style>
</head>
<body>
<div class="letterhead">
  <header class="brand">
    <div class="brand-mark"></div>
    <div class="brand-name">CORWELL TILING LTD</div>
  </header>

  <div class="rule rule-top"><span></span><span></span><span></span><span></span><span></span><span></span><span></span><span></span><span></span><span></span><span></span><span></span><span></span></div>

  <div class="rule rule-bottom"><span></span><span></span><span></span><span></span><span></span><span></span><span></span><span></span><span></span><span></span><span></span><span></span><span></span></div>

  <footer class="footer">
    <div class="registered">
      <div class="row">&nbsp;41 Birch Lane Failsworth Manchester M359QT</div>
      <div class="row"><span class="label">Company no.</span><span>5267093</span></div>
      <div class="row"><span class="label">VAT no.</span><span>412957386</span></div>
    </div>
    <div class="contact">
      <span>Mobile / Office</span><span>07831659047 &nbsp;/&nbsp; 0161 574 8192</span>
      <span>Website</span><span>www.floorvane.co.uk</span>
      <span>Email</span><span>gareth@floorvane.co.uk</span>
    </div>
  </footer>
</div>
</body>
</html>
```